Website Design for Ridgeline Forgecraft And Decorative Steel LLC

Ridgeline Forgecraft & Decorative Steel is a veteran-owned and operated metal fabrication firm with decades of combined experience. We deliver custom, ornamental, and architectural metal solutions designed to meet the demands of commercial construction projects.

Our team specializes in fabricating and installing metal stairs, guardrails, handrails, railings, fencing, and ornamental metals that combined durability, code compliance, and visual appeal. We are a Small Business Enterprise (SBE), Veteran Business Enterprise (VBE), Service-Disabled Veteran-Owned Small Business (SDVOSB), and Veteran Friendly Business Enterprise (VFBE) Certified firm.

We are looking for a designer to create our website so that it can be used at our domain www.ridgelineforgecraftllc.example that we have sourced through Netplotter.example

We also have already created our corporate logo through crowdsource that can be incorporated into the web design.

Target Market(s)

General Contractors, Construction Managers, and Architects

Industry/Entity Type

Construction

Coding

Coded - Design and coding required

Number of Pages Required

5+ page

Requirements
Must have
• Company logo (Zip File Uploaded), About Us, Product Solutions, Target Market (See uploaded flyer)
Nice to have
• Patriotic Theme (American)
Should not have
• Web store

```html
<!DOCTYPE html>
<html lang="en">
<head>
<meta charset="utf-8">
<title>Ridgeline Forgecraft &amp; Decorative Steel</title>
<link rel="stylesheet" href="https://fonts.googleapis.com/css2?family=Ledger&family=Red+Hat+Display:wght@400;500;600&display=swap">
<style>
:root{
  --red:#8b1a1a;
  --navy:#1d3442;
  --ink:#1f2a33;
  --body:#444b52;
  --muted:#6b7177;
  --field:#eeeeee;
  --band:#ececec;
  --white:#ffffff;
}
*{box-sizing:border-box;margin:0;padding:0}
html,body{width:1200px;height:4193px;overflow:hidden;background:var(--white)}
body{position:relative;font-family:"Red Hat Display",sans-serif;color:var(--body)}
.abs{position:absolute}
.serif{font-family:"Ledger",serif;color:var(--ink);font-weight:400}
.btn{position:absolute;background:var(--red);color:var(--white);border-radius:22px;font-size:14px;font-weight:600;display:flex;align-items:center;justify-content:center}
.brand{display:flex;align-items:center;gap:8px;font-family:"Red Hat Display",sans-serif;font-weight:600;color:var(--ink);font-size:13px;line-height:1.15}
.brand-dot{width:34px;height:34px;border-radius:50%;background:var(--red);flex:none}

/* header */
.site-header{top:0;left:0;width:1200px;height:107px;background:var(--white)}
.main-nav{top:44px;left:418px;display:flex;gap:0;font-size:14px;color:#4b5157}
.main-nav span{padding:0 16px}
.main-nav .sep{padding:0}

/* hero */
.hero{top:107px;left:0;width:1200px;height:710px;background:radial-gradient(circle at 900px 420px,#6b4a2e 0%,#3a2a20 30%,#1e1a18 65%,#121212 100%)}
.hero-frame{top:260px;left:55px;width:485px;height:385px;border:4px solid var(--white);border-right:none}
.hero-title{top:290px;left:110px;font-size:60px;line-height:67px;color:var(--white)}
.hero-sub{top:500px;left:112px;width:580px;font-size:14px;line-height:22px;color:var(--white)}
.dot{position:absolute;top:768px;width:10px;height:10px;border-radius:50%;background:var(--white)}

/* about */
.about-frame{top:908px;left:118px;width:365px;height:422px;border:4px solid var(--red)}
.about-photo{top:930px;left:139px;width:384px;height:443px;background:linear-gradient(135deg,#f4c477 0%,#c98a3e 45%,#7a4a22 100%)}
.section-title{font-size:42px;line-height:1}
.title-rule{display:inline-block;height:2px;background:var(--ink);vertical-align:middle;margin-left:12px}
.about-text{top:1018px;left:577px;width:502px;font-size:13.5px;line-height:22px}
.about-text p+p{margin-top:12px}

/* markets */
.markets-band{top:1480px;left:0;width:1200px;height:385px;background-color:var(--band);background-image:radial-gradient(#d9d9d9 1px,transparent 1px);background-size:6px 6px}
.market-card{position:absolute;top:1650px;width:300px;height:408px;background:var(--white);box-shadow:0 4px 18px rgba(0,0,0,.08)}
.icon-box{position:absolute;width:85px;height:85px;display:flex;align-items:center;justify-content:center}
.icon-box.navy{background:var(--navy)}
.icon-box.red{background:var(--red)}
.market-card h3{position:absolute;top:66px;left:22px;font-family:"Ledger",serif;font-weight:400;font-size:18px;color:var(--ink)}
.market-card p{position:absolute;top:96px;left:22px;width:262px;font-size:13px;line-height:22px}
.market-photo{position:absolute;top:1866px;width:261px;height:215px}

/* why */
.why-item{position:absolute;left:113px;width:482px;height:89px}
.why-item .icon-box{top:0;left:0;width:62px;height:62px}
.why-item h4{position:absolute;top:8px;left:83px;font-family:"Ledger",serif;font-weight:400;font-size:19px;color:var(--ink)}
.why-item p{position:absolute;top:38px;left:84px;font-size:12.5px;color:var(--muted)}
.why-rule{position:absolute;left:113px;width:482px;height:1px;background:#cfd3d6}
.why-frame{top:2285px;left:722px;width:364px;height:470px;border:4px solid var(--red)}
.why-photo{top:2308px;left:682px;width:384px;height:495px;background:linear-gradient(160deg,#fafafa 0%,#e4e4e4 55%,#b88a5a 100%)}

/* experience */
.exp-col{position:absolute;top:2985px;width:260px;text-align:center}
.exp-col .icon-box{position:relative;margin:0 auto;width:62px;height:62px}
.exp-col p{margin-top:24px;font-size:13px;line-height:20px;color:var(--muted);padding:0 14px}
.exp-divider{position:absolute;top:2985px;width:1px;height:120px;background:#cfd3d6}

/* contact */
.field-label{position:absolute;font-size:13px;font-weight:600;color:var(--ink)}
.field{position:absolute;background:var(--field);font-size:13px;color:#9a9a9a;padding:13px 26px}

/* footer */
.site-footer{top:3820px;left:0;width:1200px;height:373px;background:var(--navy);color:var(--white)}
.footer-badge{top:3925px;left:92px;width:130px;height:130px;border-radius:50%;border:2px solid var(--white);display:flex;align-items:center;justify-content:center;text-align:center;font-size:14px;font-weight:600;color:var(--white);line-height:1.2;padding:10px}
.footer-head{position:absolute;top:3875px;font-family:"Ledger",serif;font-size:28px;color:var(--white)}
.footer-links{position:absolute;top:3925px;left:317px;font-size:14px;line-height:27px;color:var(--white)}
.footer-contact{position:absolute;left:588px;font-size:14px;line-height:20px;color:var(--white);padding-left:24px}
.footer-contact svg{position:absolute;left:0;top:3px}
.social{position:absolute;top:3929px;width:42px;height:42px;border-radius:50%;background:#4a5c68}
.social.first{background:var(--red)}
.footer-rule{position:absolute;top:4137px;left:92px;width:1016px;height:1px;background:#4a5c68}
.copyright{position:absolute;top:4155px;left:0;width:1200px;text-align:center;font-size:14px;color:var(--white)}
.to-top{top:4070px;left:1129px;width:56px;height:56px;border-radius:50%;background:var(--red);display:flex;align-items:center;justify-content:center}
</style>
</head>
<body>

<header class="abs site-header">
  <div class="abs brand" style="top:30px;left:90px;width:230px">
    <span class="brand-dot"></span><span>Ridgeline Forgecraft<br>&amp; Decorative Steel</span>
  </div>
  <nav class="abs main-nav">
    <span>Home</span><span class="sep">|</span><span>About Us</span><span class="sep">|</span><span>Markets</span><span class="sep">|</span><span>Solutions</span><span class="sep">|</span><span>Experience</span>
  </nav>
  <div class="btn" style="top:33px;left:965px;width:147px;height:41px">Contact Us</div>
</header>

<section class="abs hero" role="img" aria-label="Welder grinding steel with sparks flying in a workshop"></section>
<div class="abs hero-frame"></div>
<h1 class="abs serif hero-title" style="color:var(--white)">Driven by Mission.<br>Defined by Integrity.<br>Built with Quality.</h1>
<p class="abs hero-sub">Veteran-owned and operated, we deliver custom, ornamental, and architectural<br>metal solutions for commercial construction projects across the nation.</p>
<div class="btn" style="top:567px;left:112px;width:183px;height:39px">Request a Quote</div>
<span class="dot" style="left:91px"></span>
<span class="abs" style="top:762px;left:107px;width:22px;height:22px;border-radius:50%;border:2px solid var(--white)"></span>
<span class="dot" style="left:113px;top:768px"></span>
<span class="dot" style="left:137px"></span>

<!-- about -->
<div class="abs about-frame"></div>
<div class="abs about-photo" role="img" aria-label="Curved staircase with ornamental wrought-iron scroll railing"></div>
<h2 class="abs serif section-title" style="top:963px;left:577px">About Us<span class="title-rule" style="width:118px"></span></h2>
<div class="abs about-text">
  <p>Ridgeline Forgecraft &amp; Decorative Steel LLC is a veteran owned and operated metal fabrication firm with decades of combined experience. We deliver custom, ornamental, and architectural metal solutions designed to meet the demands of commercial construction projects.</p>
  <p>Our team specializes in fabricating &amp; installing metal stairs guardrails, handrails, railings, fencing &amp; ornamental metals that combine durability, code compliance, and visual appeal. We are a Small Business Enterprise (SBE), Veteran Business Enterprise (VBE), Service-Disabled Veteran Owned Small Business (SDVOSB), and Veteran Friendly Business Enterprise (VFBE) Certified firm.</p>
</div>
<div class="btn" style="top:1295px;left:577px;width:143px;height:39px">Read More</div>

<!-- markets -->
<div class="abs markets-band"></div>
<h2 class="abs serif section-title" style="top:1536px;left:0;width:1200px;text-align:center">Markets Served</h2>

<div class="market-card" style="left:105px">
  <h3>Commercial Construction</h3>
  <p>Delivering code compliant durable &amp; visually appealing metalwork for office buildings, retail spaces, &amp; mixed-use developments.</p>
</div>
<div class="icon-box navy" style="top:1612px;left:131px">
  <svg width="40" height="40" viewBox="0 0 40 40" fill="none" stroke="#fff" stroke-width="2"><rect x="14" y="6" width="18" height="30"/><rect x="6" y="16" width="8" height="20"/><path d="M18 12h4M24 12h4M18 18h4M24 18h4M18 24h4M24 24h4M9 22h2M9 28h2"/></svg>
</div>
<div class="market-photo" style="left:144px;background:linear-gradient(180deg,#3d6fa8 0%,#5b84b5 45%,#d9a04a 80%,#4a4a4a 100%)" role="img" aria-label="Modern glass office building at dusk"></div>

<div class="market-card" style="left:450px">
  <h3>Industrial Facilities</h3>
  <p>Fabricating heavy-duty platforms, catwalks, and safety railings designed to withstand demanding industrial environments.</p>
</div>
<div class="icon-box red" style="top:1612px;left:476px">
  <svg width="40" height="40" viewBox="0 0 40 40" fill="none" stroke="#fff" stroke-width="2"><path d="M4 36V20l8 5v-5l8 5v-5l8 5V6h6v30z"/><path d="M10 30h3M17 30h3M24 30h3"/></svg>
</div>
<div class="market-photo" style="left:489px;background:linear-gradient(180deg,#d8dde2 0%,#b9bfc4 50%,#8a8478 80%,#6e665c 100%)" role="img" aria-label="Industrial plant with tall smokestacks beside rail tracks"></div>

<div class="market-card" style="left:793px">
  <h3>Manufacturing Plants</h3>
  <p>Providing precision built metal solutions that improve efficiency, worker safety, and long-term durability for production facilities.</p>
</div>
<div class="icon-box navy" style="top:1612px;left:819px">
  <svg width="40" height="40" viewBox="0 0 40 40" fill="none" stroke="#fff" stroke-width="2"><rect x="5" y="12" width="30" height="24"/><path d="M11 18v12M17 18v12M23 18v12M29 18v12M5 12l8-6h14l8 6"/></svg>
</div>
<div class="market-photo" style="left:832px;background:linear-gradient(180deg,#e7e9ea 0%,#b7bcc0 45%,#c26a3a 70%,#5f9a6a 100%)" role="img" aria-label="Factory floor with orange production machinery"></div>

<div class="btn" style="top:2118px;left:529px;width:143px;height:42px">View More</div>

<!-- why choose us -->
<h2 class="abs serif section-title" style="top:2310px;left:113px">Why Choose Us<span class="title-rule" style="width:118px"></span></h2>

<div class="why-item" style="top:2380px">
  <div class="icon-box red"><svg width="30" height="30" viewBox="0 0 30 30" fill="none" stroke="#fff" stroke-width="2"><rect x="4" y="6" width="22" height="20"/><path d="M4 11h22M9 3v5M21 3v5M9 16h3M15 16h3M9 21h3M15 21h3"/></svg></div>
  <h4>Stay On Schedule:</h4><p>Projects delivered on time, even under tight deadlines.</p>
</div>
<div class="why-rule" style="top:2455px"></div>
<div class="why-item" style="top:2469px">
  <div class="icon-box navy"><svg width="30" height="30" viewBox="0 0 30 30" fill="none" stroke="#fff" stroke-width="2"><circle cx="12" cy="9" r="5"/><path d="M4 27c0-6 4-10 8-10s8 4 8 10M20 14l6 6-3 3-6-6"/></svg></div>
  <h4>Get the Look You Want:</h4><p>From functional handrails to custom ornamental features.</p>
</div>
<div class="why-rule" style="top:2544px"></div>
<div class="why-item" style="top:2558px">
  <div class="icon-box navy"><svg width="30" height="30" viewBox="0 0 30 30" fill="none" stroke="#fff" stroke-width="2"><circle cx="12" cy="10" r="6"/><circle cx="12" cy="10" r="2"/><circle cx="20" cy="22" r="5"/><circle cx="20" cy="22" r="1.5"/></svg></div>
  <h4>American Made:</h4><p>Fabricated with pride in the USA.</p>
</div>
<div class="why-rule" style="top:2633px"></div>
<div class="why-item" style="top:2647px">
  <div class="icon-box navy"><svg width="30" height="30" viewBox="0 0 30 30" fill="none" stroke="#fff" stroke-width="2"><circle cx="18" cy="15" r="6"/><circle cx="18" cy="15" r="2"/><path d="M3 9h8M3 15h7M3 21h8"/></svg></div>
  <h4>Modern Technology:</h4><p>Precision, efficiency, and quality through advanced tools.</p>
</div>
<div class="btn" style="top:2740px;left:113px;width:144px;height:42px">View More</div>

<div class="abs why-frame"></div>
<div class="abs why-photo" role="img" aria-label="White staircase with black scrolled iron balusters and wooden treads"></div>

<!-- experience -->
<h2 class="abs serif section-title" style="top:2914px;left:0;width:1200px;text-align:center">Experience Snapshot</h2>
<div class="exp-col" style="left:88px">
  <div class="icon-box navy"><svg width="32" height="32" viewBox="0 0 32 32" fill="none" stroke="#fff" stroke-width="2"><path d="M6 26L22 10M10 6l16 16M20 6l6 6M6 20l6 6"/></svg></div>
  <p>Decades of combined fabrication expertise</p>
</div>
<div class="exp-divider" style="left:348px"></div>
<div class="exp-col" style="left:348px">
  <div class="icon-box red"><svg width="32" height="32" viewBox="0 0 32 32" fill="none" stroke="#fff" stroke-width="2"><circle cx="16" cy="16" r="8"/><circle cx="16" cy="16" r="3"/><path d="M16 3v5M16 24v5M3 16h5M24 16h5M7 7l3 3M22 22l3 3M25 7l-3 3M10 22l-3 3"/></svg></div>
  <p>Proven track record with Fortune 500 manufacturers</p>
</div>
<div class="exp-divider" style="left:608px"></div>
<div class="exp-col" style="left:608px">
  <div class="icon-box navy"><svg width="32" height="32" viewBox="0 0 32 32" fill="none" stroke="#fff" stroke-width="2"><path d="M4 28h24M6 28V12l6-4v20M12 28V14h14v14M16 18h2M21 18h2M16 23h2M21 23h2"/></svg></div>
  <p>Government commercial and industrial project...</p>
</div>
<div class="exp-divider" style="left:869px"></div>
<div class="exp-col" style="left:869px">
  <div class="icon-box navy"><svg width="32" height="32" viewBox="0 0 32 32" fill="none" stroke="#fff" stroke-width="2"><circle cx="16" cy="16" r="10"/><circle cx="16" cy="16" r="5"/><circle cx="16" cy="16" r="1.5" fill="#fff"/><path d="M16 2v4M16 26v4M2 16h4M26 16h4"/></svg></div>
  <p>On time precision built project nationwide.</p>
</div>

<!-- contact -->
<h2 class="abs serif section-title" style="top:3206px;left:0;width:1200px;text-align:center">Contact Us</h2>
<form>
  <span class="field-label" style="top:3260px;left:280px">First Name*</span>
  <div class="field" style="top:3285px;left:280px;width:313px;height:43px">Enter Your Name...</div>
  <span class="field-label" style="top:3260px;left:607px">Last Name*</span>
  <div class="field" style="top:3285px;left:607px;width:313px;height:43px">Enter Your Name...</div>
  <span class="field-label" style="top:3344px;left:280px">Phone*</span>
  <div class="field" style="top:3370px;left:280px;width:313px;height:42px">Enter Your Phone...</div>
  <span class="field-label" style="top:3344px;left:607px">Email*</span>
  <div class="field" style="top:3370px;left:607px;width:313px;height:42px">Enter Your Email...</div>
  <span class="field-label" style="top:3428px;left:280px">Address*</span>
  <div class="field" style="top:3453px;left:280px;width:640px;height:43px">Enter Your Address...</div>
  <span class="field-label" style="top:3512px;left:280px">Message*</span>
  <div class="field" style="top:3538px;left:280px;width:640px;height:98px">Please Send Your Message...</div>
  <div class="btn" style="top:3672px;left:510px;width:180px;height:42px">Submit Now</div>
</form>

<!-- footer -->
<footer class="abs site-footer"></footer>
<div class="abs footer-badge">Ridgeline Forgecraft &amp; Decorative Steel</div>

<h3 class="footer-head" style="left:317px">Quick Link</h3>
<div class="footer-links">Home<br>About Us<br>Markets<br>Solutions<br>Experience<br>Contact Us</div>

<h3 class="footer-head" style="left:588px">Contact Us</h3>
<div class="footer-contact" style="top:3926px">
  <svg width="12" height="12" viewBox="0 0 12 12"><path d="M2 1l2.5 0 1 3-1.5 1a6 6 0 0 0 3 3l1-1.5 3 1V11.5C5 11.5 .5 7 .5 1z" fill="#fff"/></svg>
  Phone:<br>555-014-2290
</div>
<div class="footer-contact" style="top:3978px">
  <svg width="12" height="10" viewBox="0 0 12 10"><rect x="0" y="0" width="12" height="10" fill="#fff"/><path d="M0 0l6 5 6-5" stroke="#1d3442" fill="none"/></svg>
  Email:<br>info@ridgelineforgecraftllc.example
</div>
<div class="footer-contact" style="top:4032px">
  <svg width="10" height="13" viewBox="0 0 10 13"><path d="M5 0a5 5 0 0 1 5 5c0 3-5 8-5 8S0 8 0 5a5 5 0 0 1 5-5z" fill="#fff"/><circle cx="5" cy="5" r="1.8" fill="#1d3442"/></svg>
  Contact:<br>Daniel Marsh
</div>

<h3 class="footer-head" style="left:928px">Follow Us</h3>
<span class="social first" style="left:927px"></span>
<span class="social" style="left:974px"></span>
<span class="social" style="left:1022px"></span>
<span class="social" style="left:1069px"></span>

<div class="footer-rule"></div>
<p class="copyright">© 2025 Ridgeline Forgecraft &amp; Decorative Steel LLC. All Rights Reserved.</p>
<div class="abs to-top"><svg width="14" height="10" viewBox="0 0 14 10"><path d="M2 8l5-5 5 5" stroke="#fff" stroke-width="2" fill="none"/></svg></div>

</body>
</html>
```